Kestrel Summit 2019 Enemies of the End-Times Church Flyer

We want a church conference flyer designed. We are looking for a professional, yet catchy design that uses our brand colors and logo creatively while communicating key information of the event effectively. <br/>The flyer must include all of the following:<br/>Title: Kestrel Summit 2019<br/>Topic: The Enemies of The End-Times Church <br/>Subtitles: <br/> -How the antichrist raises an army by social behavior engineering. <br/>-How the architects of modern social constructs escaped the church's radar. <br/>-The Holy Spirit's end-times agenda:<br/> The Knock-Out Punch!<br/>Speaker: Prophet Marcus Toliver <br/>Dates/time: December 27, 28 & 29 at 6pm<br/>Location: Halvorn Community Center <br/> 241 Pellham Street <br/> Portland, ME 04102<br/>Contact info: phone: 207-555-0148 <br/>email: contact@brookmeadow.example <br/> www.vutel.example<br/>*The flyer must also include a picture of the speaker and our Vutel logo <br/>Thanks, we look forward to seeing what you come up with!

Colors

Designer to choose colors to be used in the design.

Requirements
Must have
• The flyer must include all of the following:
• Title: Kestrel Summit 2019
• Topic: The Enemies of The End-Times Church
• Subtitles:
• -How the antichrist raises an army by social behavior engineering.
• -How the architects of modern social constructs escaped the church's radar.
• -The Holy Spirit's end-times agenda:
• The Knock-Out Punch!
• Speaker: Prophet Marcus Toliver
• Dates/time: December 27, 28 & 29 at 6pm
• Location: Halvorn Community Center
• 241 Pellham Street
• Portland, ME 04102
• Contact info: phone: 207-555-0148
• email: contact@brookmeadow.example
• www.vutel.example
• *The flyer must also include a picture of the speaker and our Vutel logo
Should not have
• Pictures of crosses or church buildings

```html
<!DOCTYPE html>
<html lang="en">
<head>
<meta charset="utf-8">
<title>Kestrel Summit 2019 – Flyer Options</title>
<link rel="stylesheet" href="https://fonts.googleapis.com/css2?family=Crimson+Text:ital,wght@0,400;0,600;0,700;1,600;1,700&family=Playfair+Display:ital,wght@0,700;1,700&family=Open+Sans:wght@400;600;700&display=swap">
<style>
  :root {
    --navy: #1f3a5f;
    --orange: #f3861f;
    --red: #d63a1f;
    --white: #ffffff;
    --paper-tint: #f4f6f9;
    --rule: #9aa6b6;
    --photo-a: #5b5f66;
    --photo-b: #2c2f35;
  }
  * { box-sizing: border-box; margin: 0; padding: 0; }
  html, body { width: 1200px; height: 840px; overflow: hidden; background: var(--white); }
  body { position: relative; font-family: "Open Sans", sans-serif; color: var(--navy); }

  .flyer {
    position: absolute; top: 15px; width: 565px; height: 810px;
    background: var(--white); overflow: hidden;
    box-shadow: 0 0 0 1px #e3e3e3;
  }
  .flyer--a { left: 15px; }
  .flyer--b { left: 620px; }
  .flyer__shapes { position: absolute; inset: 0; width: 565px; height: 810px; }
  .flyer > *:not(.flyer__shapes) { position: absolute; }

  .event-title {
    left: 28px; top: 26px; width: 250px;
    font-family: "Crimson Text", serif; font-weight: 600;
    font-size: 48px; line-height: 1.02; color: var(--navy); text-align: center;
  }
  .brand {
    right: 30px; top: 36px; display: flex; align-items: center; gap: 8px;
    font-family: "Crimson Text", serif; font-weight: 700; font-size: 40px;
    color: var(--navy); letter-spacing: 1px;
  }
  .brand__dot { width: 14px; height: 14px; border-radius: 50%; background: var(--orange); }

  .speaker-photo {
    left: 36px; top: 222px; width: 170px; height: 212px;
    background: linear-gradient(160deg, var(--photo-a), var(--photo-b));
  }

  .topic {
    left: 262px; top: 195px; white-space: nowrap;
    font-family: "Playfair Display", serif; font-weight: 700; color: var(--navy);
  }
  .topic__the { display: block; font-style: italic; color: var(--red); font-size: 40px; line-height: 1; margin-left: 10px; }
  .topic__row { display: flex; align-items: flex-end; }
  .topic__cap { font-size: 110px; line-height: 0.8; }
  .topic__rest { display: flex; flex-direction: column; margin-left: 2px; }
  .topic__word { font-size: 38px; line-height: 1; }
  .topic__small { font-size: 16px; line-height: 1; margin-left: 64px; }
  .topic__last { display: block; font-size: 38px; line-height: 1.05; margin-left: 150px; font-weight: 400; }

  .speaker { left: 0; top: 436px; height: 40px; padding: 3px 0 0 28px; color: var(--white); font-size: 14px; line-height: 1.15; }
  .flyer--a .speaker { width: 275px; }
  .flyer--b .speaker { width: 240px; }
  .speaker__label, .speaker__name { display: block; }
  .speaker__label { font-weight: 700; }
  .speaker__name { font-weight: 600; }

  .topics { list-style: none; font-family: "Crimson Text", serif; font-style: italic; font-weight: 700; font-size: 16px; line-height: 1.1; text-align: center; }
  .flyer--a .topics { left: 285px; top: 378px; width: 235px; color: var(--navy); }
  .flyer--a .topics li { padding: 8px 0; border-bottom: 2px solid var(--rule); }
  .flyer--a .topics li:last-child { border-bottom: 0; }

  .when { font-family: "Crimson Text", serif; font-weight: 700; color: var(--orange); line-height: 1.05; white-space: nowrap; }
  .where { font-family: "Crimson Text", serif; font-weight: 700; color: var(--navy); line-height: 1.1; white-space: nowrap; }
  .where span { display: block; }

  .contact { color: var(--white); }
  .contact__title { font-family: "Crimson Text", serif; font-weight: 700; font-size: 24px; line-height: 1.2; color: var(--orange); margin-bottom: 10px; }
  .contact__line { display: flex; align-items: center; gap: 12px; font-size: 16px; line-height: 22px; margin-bottom: 12px; white-space: nowrap; }
  .contact__line svg { width: 20px; height: 20px; flex: none; }

  .web { right: 26px; bottom: 8px; font-family: "Crimson Text", serif; font-weight: 700; font-size: 24px; line-height: 1.2; color: var(--navy); }

  /* Option A */
  .flyer--a .when { left: 28px; top: 545px; font-size: 26px; }
  .flyer--a .where { left: 28px; top: 640px; font-size: 16px; }
  .flyer--a .where span { margin-bottom: 8px; }
  .flyer--a .contact { left: 240px; top: 630px; }

  /* Option B */
  .flyer--b .when { left: 256px; top: 385px; font-size: 24px; }
  .flyer--b .where { left: 405px; top: 385px; font-size: 17px; }
  .flyer--b .where span { margin-bottom: 6px; }
  .flyer--b .topics { left: 0; top: 0; width: 565px; height: 810px; color: var(--white); font-size: 17px; }
  .flyer--b .topics li { position: absolute; }
  .flyer--b .topic-1 { left: 20px; top: 545px; width: 230px; }
  .flyer--b .topic-2 { left: 240px; top: 615px; width: 290px; }
  .flyer--b .topic-3 { left: 370px; top: 690px; width: 175px; text-align: right; }
  .flyer--b .contact { left: 28px; top: 668px; }
</style>
</head>
<body>

<article class="flyer flyer--a">
  <svg class="flyer__shapes" viewBox="0 0 565 810" aria-hidden="true">
    <defs>
      <linearGradient id="warmA" x1="0" y1="0" x2="1" y2="1">
        <stop offset="0" stop-color="#f7a033"/><stop offset="0.55" stop-color="#ef6a1f"/><stop offset="1" stop-color="#d63a1f"/>
      </linearGradient>
    </defs>
    <path d="M250,0 H565 V190 C470,175 370,185 320,120 C295,85 270,45 250,0Z" fill="url(#warmA)"/>
    <path d="M540,330 C558,390 565,430 565,470 V590 C552,550 540,500 532,460Z" fill="url(#warmA)"/>
    <path d="M0,190 C20,170 30,120 0,100Z" fill="url(#warmA)"/>
    <path d="M0,500 C60,520 120,535 200,538 C160,560 140,600 150,765 H0Z" fill="var(--paper-tint)"/>
    <rect x="0" y="436" width="275" height="40" fill="var(--navy)"/>
    <path d="M225,765 C215,660 260,600 360,590 C450,580 520,585 565,560 V765Z" fill="var(--navy)"/>
  </svg>

  <h1 class="event-title">Kestrel Summit 2019</h1>
  <div class="brand"><span class="brand__dot"></span>VUTEL</div>
  <div class="speaker-photo" role="img" aria-label="Portrait photo of speaker Prophet Marcus Toliver"></div>

  <h2 class="topic">
    <span class="topic__the">The</span>
    <span class="topic__row"><span class="topic__cap">E</span><span class="topic__rest"><span class="topic__word">nemies of</span><span class="topic__small">the</span><span class="topic__word">End-Times</span></span></span>
    <span class="topic__last">church</span>
  </h2>

  <p class="speaker"><span class="speaker__label">Speaker</span><span class="speaker__name">Prophet Marcus Toliver</span></p>

  <ul class="topics">
    <li>How the antichrist raises an army by social behavior engineering</li>
    <li>How the architects of modern social constructs escaped the church's radar</li>
    <li>The Holy Spirit's end-times agenda</li>
  </ul>

  <p class="when">December<br>27, 28 &amp; 29<br>at 6pm</p>
  <p class="where"><span>Halvorn<br>Community<br>Center</span><span>241 Pellham<br>Street</span><span>Portland,<br>ME 04102</span></p>

  <div class="contact">
    <p class="contact__title">Contact info</p>
    <p class="contact__line"><svg viewBox="0 0 24 24"><path fill="#fff" d="M6.6 10.8a15.1 15.1 0 0 0 6.6 6.6l2.2-2.2c.3-.3.7-.4 1-.2 1.1.4 2.3.6 3.6.6.6 0 1 .4 1 1V20c0 .6-.4 1-1 1A17 17 0 0 1 3 4c0-.6.4-1 1-1h3.5c.6 0 1 .4 1 1 0 1.3.2 2.5.6 3.6.1.3 0 .7-.2 1z"/></svg>207-555-0148</p>
    <p class="contact__line"><svg viewBox="0 0 24 24"><rect x="2" y="5" width="20" height="14" rx="1" fill="#fff"/><path d="M2.5 6 12 13l9.5-7" fill="none" stroke="var(--navy)" stroke-width="1.6"/></svg>contact@brookmeadow.example</p>
  </div>

  <p class="web">www.vutel.example</p>
</article>

<article class="flyer flyer--b">
  <svg class="flyer__shapes" viewBox="0 0 565 810" aria-hidden="true">
    <defs>
      <linearGradient id="warmB" x1="0" y1="0" x2="1" y2="1">
        <stop offset="0" stop-color="#f7a033"/><stop offset="0.55" stop-color="#ef6a1f"/><stop offset="1" stop-color="#d63a1f"/>
      </linearGradient>
    </defs>
    <path d="M250,0 H565 V190 C470,175 370,185 320,120 C295,85 270,45 250,0Z" fill="url(#warmB)"/>
    <path d="M0,190 C20,170 30,120 0,100Z" fill="url(#warmB)"/>
    <path d="M0,480 C150,500 280,565 400,568 C480,570 530,562 565,552 V770 H0Z" fill="var(--navy)"/>
    <path d="M0,476 C150,496 280,561 400,564 C480,566 530,558 565,548 V556 C530,566 480,574 400,572 C280,569 150,504 0,484Z" fill="var(--orange)"/>
    <rect x="0" y="436" width="240" height="40" fill="var(--navy)"/>
  </svg>

  <h1 class="event-title">Kestrel Summit 2019</h1>
  <div class="brand"><span class="brand__dot"></span>VUTEL</div>
  <div class="speaker-photo" role="img" aria-label="Portrait photo of speaker Prophet Marcus Toliver"></div>

  <h2 class="topic">
    <span class="topic__the">The</span>
    <span class="topic__row"><span class="topic__cap">E</span><span class="topic__rest"><span class="topic__word">nemies of</span><span class="topic__small">the</span><span class="topic__word">End-Times</span></span></span>
    <span class="topic__last">church</span>
  </h2>

  <p class="speaker"><span class="speaker__label">Speaker</span><span class="speaker__name">Prophet Marcus Toliver</span></p>

  <p class="when">December<br>27, 28 &amp; 29<br>at 6pm</p>
  <p class="where"><span>Halvorn<br>Community<br>Center</span><span>241 Pellham<br>Street</span><span>Portland,<br>ME 04102</span></p>

  <ul class="topics">
    <li class="topic-1">How the antichrist raises an army by social behavior engineering</li>
    <li class="topic-2">How the architects of modern social constructs escaped the church's radar</li>
    <li class="topic-3">The Holy Spirit's end-times agenda</li>
  </ul>

  <div class="contact">
    <p class="contact__title">Contact info</p>
    <p class="contact__line"><svg viewBox="0 0 24 24"><path fill="#fff" d="M6.6 10.8a15.1 15.1 0 0 0 6.6 6.6l2.2-2.2c.3-.3.7-.4 1-.2 1.1.4 2.3.6 3.6.6.6 0 1 .4 1 1V20c0 .6-.4 1-1 1A17 17 0 0 1 3 4c0-.6.4-1 1-1h3.5c.6 0 1 .4 1 1 0 1.3.2 2.5.6 3.6.1.3 0 .7-.2 1z"/></svg>207-555-0148</p>
    <p class="contact__line"><svg viewBox="0 0 24 24"><rect x="2" y="5" width="20" height="14" rx="1" fill="#fff"/><path d="M2.5 6 12 13l9.5-7" fill="none" stroke="var(--navy)" stroke-width="1.6"/></svg>contact@brookmeadow.example</p>
  </div>

  <p class="web">www.vutel.example</p>
</article>

</body>
</html>
```